Health care technology software systems

We have a solid logo. We have company colors that will need to be used as well. We just need a great business card design. We sell to health plans but want to be modern
Updates

Need extra days to review

Target Market(s)

Health technology sector selling into Health Plans

Industry/Entity Type

Health Care Technology

Contact Information for Business Card

Name, title, address, phone number, email

Requirements
Must have
• Use of Kembrata corporate colors - Uploaded w/ our logos

```html
<!DOCTYPE html>
<html lang="en">
<head>
<meta charset="utf-8">
<title>Kembrata Business Card</title>
<link href="https://fonts.googleapis.com/css2?family=Open+Sans:wght@300;400;700&display=swap" rel="stylesheet">
<style>
  :root {
    --stage: #2b2c2e;
    --navy: #34539f;
    --sky: #16a1dc;
    --lime: #7cb93a;
    --paper: #f3f4f5;
    --rim: #c9cbcd;
    --ink: #3a3a3c;
    --muted: #5a5b5d;
    --front-core: #1f95d8;
    --front-edge: #3b64b8;
  }
  * { box-sizing: border-box; margin: 0; padding: 0; }
  html, body { width: 1200px; height: 900px; overflow: hidden; }
  body {
    background: var(--stage);
    font-family: "Open Sans", Arial, sans-serif;
    position: relative;
  }

  /* Front side */
  .card-front {
    position: absolute;
    left: 90px; top: 110px;
    width: 540px; height: 309px;
    background: radial-gradient(circle at 52% 55%, var(--front-core) 0%, #2a82cf 45%, var(--front-edge) 100%);
    overflow: hidden;
  }
  .card-front .halo { position: absolute; inset: 0; }
  .front-brand {
    position: absolute;
    left: 0; right: 0; top: 120px;
    display: flex; align-items: center; justify-content: center; gap: 16px;
  }
  .front-brand .dot {
    width: 52px; height: 52px; border-radius: 50%;
    background: #ffffff;
  }
  .front-brand .wordmark {
    font-weight: 300; font-size: 62px; line-height: 1;
    color: #ffffff; letter-spacing: 1px;
  }

  /* Back side */
  .card-back {
    position: absolute;
    left: 560px; top: 480px;
    width: 580px; height: 332px;
    overflow: hidden;
  }
  .card-back .shapes { position: absolute; inset: 0; }
  .holder {
    position: absolute; left: 170px; top: 50px;
    text-align: center;
  }
  .holder .name {
    font-weight: 700; font-size: 17px; color: var(--sky); letter-spacing: 0.5px;
  }
  .holder .role {
    font-size: 14px; color: var(--muted); line-height: 1.2;
  }
  .back-brand {
    position: absolute; left: 170px; top: 98px;
    display: flex; align-items: center; gap: 14px;
  }
  .back-brand .dot {
    width: 44px; height: 44px; border-radius: 50%; background: var(--sky);
  }
  .back-brand .wordmark {
    font-weight: 300; font-size: 58px; line-height: 1; color: var(--ink); letter-spacing: 1px;
  }
  .contacts {
    position: absolute; left: 252px; top: 168px;
    list-style: none;
    font-size: 15px; color: var(--muted);
  }
  .contacts li {
    display: flex; align-items: center; gap: 7px; line-height: 21px;
  }
  .contacts li.gap { margin-top: 6px; }
  .contacts .indent { margin-left: 21px; }
  .contacts svg { width: 14px; height: 14px; flex: none; fill: var(--lime); }
  .address {
    position: absolute; left: 252px; top: 268px;
    display: flex; gap: 7px;
    font-size: 15px; color: var(--muted); line-height: 20px;
  }
  .address svg { width: 14px; height: 18px; margin-top: 2px; fill: var(--lime); flex: none; }
</style>
</head>
<body>

  <section class="card-front" aria-label="Card front">
    <svg class="halo" viewBox="0 0 540 309" aria-hidden="true">
      <circle cx="280" cy="170" r="230" fill="none" stroke="#ffffff" stroke-opacity="0.12" stroke-width="26"/>
      <circle cx="285" cy="165" r="170" fill="#ffffff" fill-opacity="0.06"/>
    </svg>
    <div class="front-brand">
      <span class="dot"></span>
      <span class="wordmark">kembrata</span>
    </div>
  </section>

  <section class="card-back" aria-label="Card back">
    <svg class="shapes" viewBox="0 0 580 332" aria-hidden="true">
      <rect width="580" height="332" fill="var(--sky)"/>
      <rect width="300" height="332" fill="var(--navy)"/>
      <polygon points="0,0 120,0 0,80" fill="var(--lime)"/>
      <polygon points="330,0 520,0 500,78" fill="var(--lime)"/>
      <circle cx="300" cy="170" r="222" fill="var(--paper)"/>
      <circle cx="305" cy="168" r="204" fill="var(--paper)" stroke="var(--rim)" stroke-width="3"/>
    </svg>

    <div class="holder">
      <div class="name">MARA ELLISON</div>
      <div class="role">Director</div>
    </div>

    <div class="back-brand">
      <span class="dot"></span>
      <span class="wordmark">kembrata</span>
    </div>

    <ul class="contacts">
      <li>
        <svg viewBox="0 0 16 16"><path d="M3 2h3l1.5 3.5-2 1.2a8 8 0 0 0 3.8 3.8l1.2-2L14 10v3a1 1 0 0 1-1 1A11 11 0 0 1 2 3a1 1 0 0 1 1-1z"/></svg>
        <span>0912345678</span>
      </li>
      <li><span class="indent">kembrata.com</span></li>
      <li class="gap">
        <svg viewBox="0 0 16 16"><path d="M1 4h14v9H1z M1 4l7 5 7-5" stroke="#fff" stroke-width="1"/></svg>
        <span>info@kembrata.com</span>
      </li>
      <li>
        <svg viewBox="0 0 16 16"><circle cx="8" cy="8" r="7"/><path d="M1 8h14M8 1c-3 3-3 11 0 14M8 1c3 3 3 11 0 14" stroke="#fff" stroke-width="1" fill="none"/></svg>
        <span>www.kembrata.com</span>
      </li>
    </ul>

    <div class="address">
      <svg viewBox="0 0 14 18"><path d="M7 0a6 6 0 0 1 6 6c0 4.5-6 12-6 12S1 10.5 1 6a6 6 0 0 1 6-6zm0 3.5a2.5 2.5 0 1 0 0 5 2.5 2.5 0 0 0 0-5z"/></svg>
      <div>24 Harbor Row, Lindell Park<br>P.O Box 4410 Westvale</div>
    </div>
  </section>

</body>
</html>
```